Garlic Farm for Farm Sales/Restaurant sales

Need a professional, but appealing to agriculture world. We are selling 27 kinds of Organic Garlic from a farm in Simla,CO. I have uploaded logo and business information-we are going to need a template, because I will need to use it for four separate people.
-We are trying to appeal to Farm to table restaurants
-As well as growers/farmers

Target Market(s)

Agriculture Sales/Restaurants-Organic

Industry/Entity Type

Agriculture

Contact Information for Business Card

Want it to look more unique then your average orbel mart card- I want it to look amazing

Font styles to use
Sans Serif

Colors
0455a3
ec1f27
fbed22
ffffff

Requirements
Must have
• Just be creative
Nice to have
• Colorful
Should not have
• plain

```html
<!DOCTYPE html>
<html lang="en">
<head>
<meta charset="utf-8">
<title>Tall Plains Gourmet Garlic – Business Card</title>
<link href="https://fonts.googleapis.com/css2?family=Cinzel:wght@500;600&family=Open+Sans:wght@400;600&display=swap" rel="stylesheet">
<style>
  :root{
    --bg:#e4d3bd;
    --card-front:#f2efe6;
    --card-back:#0d0d0d;
    --navy:#1d2a5c;
    --blue:#0455a3;
    --red:#ec1f27;
    --yellow:#fbed22;
    --white:#ffffff;
    --ink:#3a3a3a;
    --rule:#3e3e3e;
  }
  *{box-sizing:border-box;margin:0;padding:0}
  html,body{width:1200px;height:823px;overflow:hidden}
  body{
    background:var(--bg);
    font-family:"Open Sans",Arial,sans-serif;
    display:flex;align-items:center;justify-content:center;gap:40px;
  }
  .card{
    position:relative;width:560px;height:320px;border-radius:4px;
    box-shadow:0 10px 24px rgba(0,0,0,.18);overflow:hidden;
  }
  /* back side */
  .card--back{background:var(--card-back);display:flex;flex-direction:column;align-items:center;justify-content:center;gap:18px}
  .brand-mark{display:flex;align-items:center;gap:14px}
  .brand-mark__dot{width:46px;height:46px;border-radius:50%;background:var(--red);flex:none}
  .card--back .brand-mark__name{font-family:"Cinzel",Georgia,serif;font-weight:600;font-size:36px;color:var(--white);letter-spacing:1px}
  .card--back .website{color:var(--white);font-size:17px;letter-spacing:.5px}

  /* front side */
  .card--front{background:var(--card-front);color:var(--ink)}
  .company{position:absolute;left:40px;top:40px}
  .company .brand-mark__dot{width:56px;height:56px}
  .company .brand-mark__name{font-family:"Cinzel",Georgia,serif;font-weight:600;font-size:30px;color:var(--navy);line-height:1}
  .company__tagline{font-family:"Open Sans",Arial,sans-serif;font-size:13px;color:var(--red);letter-spacing:1.5px;text-transform:uppercase;margin:10px 0 0 70px}
  .person{position:absolute;right:38px;top:58px;text-align:right}
  .person__name{font-family:"Cinzel",Georgia,serif;font-weight:600;font-size:26px;color:#222}
  .person__title{font-size:13px;color:var(--blue);margin-top:2px}
  .divider{position:absolute;left:40px;right:38px;top:150px;height:1.5px;background:var(--rule)}
  .phones{position:absolute;left:40px;top:182px;list-style:none}
  .phones li,.contact .email{display:flex;align-items:center;gap:12px;font-size:16px;line-height:1;margin-bottom:12px;color:#333}
  .icon{width:22px;height:22px;flex:none}
  .contact{position:absolute;right:38px;top:182px;font-size:15px;line-height:1.5;color:#333}
  .contact address{font-style:normal;margin-bottom:14px}
  .contact .email{font-size:15px}
</style>
</head>
<body>

<section class="card card--back" aria-label="Card back">
  <div class="brand-mark">
    <span class="brand-mark__dot"></span>
    <span class="brand-mark__name">Tall Plains</span>
  </div>
  <p class="website">www.tallplainsgarlic.com</p>
</section>

<section class="card card--front" aria-label="Card front">
  <div class="company">
    <div class="brand-mark">
      <span class="brand-mark__dot"></span>
      <span class="brand-mark__name">Tall Plains</span>
    </div>
    <p class="company__tagline">Gourmet Garlic</p>
  </div>

  <div class="person">
    <h1 class="person__name">Helen R. Marsh</h1>
    <p class="person__title">Founder &amp; Executive Director</p>
  </div>

  <div class="divider"></div>

  <ul class="phones">
    <li>
      <svg class="icon" viewBox="0 0 22 22" aria-label="Office phone"><rect width="22" height="22" fill="var(--blue)"/><path d="M5 9c0-2 3-3 6-3s6 1 6 3l-2 1-1-2h-6l-1 2z M7 11h8l1 5H6z" fill="#fff"/></svg>
      (555) 214-6630
    </li>
    <li>
      <svg class="icon" viewBox="0 0 22 22" aria-label="Mobile phone"><rect width="22" height="22" fill="var(--blue)"/><rect x="7.5" y="4" width="7" height="14" rx="1.2" fill="#fff"/><rect x="8.8" y="6" width="4.4" height="6" fill="var(--blue)"/></svg>
      (555) 381-0472
    </li>
    <li>
      <svg class="icon" viewBox="0 0 22 22" aria-label="Fax"><rect width="22" height="22" fill="var(--blue)"/><rect x="7" y="4" width="8" height="5" fill="#fff"/><rect x="4" y="9" width="14" height="6" rx="1" fill="#fff"/><rect x="7" y="14" width="8" height="4" fill="#fff" stroke="var(--blue)"/></svg>
      (555) 907-1158
    </li>
  </ul>

  <div class="contact">
    <address>418 Fenwick Road<br>Suite 210 Millbrook, CO 80830</address>
    <p class="email">
      <svg class="icon" viewBox="0 0 22 22" aria-label="Email"><rect width="22" height="22" fill="var(--blue)"/><rect x="4" y="6" width="14" height="10" fill="#fff"/><path d="M4 6l7 6 7-6M4 16l5-5M18 16l-5-5" fill="none" stroke="var(--blue)" stroke-width="1.2"/></svg>
      hmarsh@tallplainsgarlic.com
    </p>
  </div>
</section>

</body>
</html>
```